website for Hotel Brisaverde
Hotel Brisaverde "en el corazon de El Estor"
El Hotel Brisaverde esta situado en el corazon de "El Estorcito Alegre"
left side
http://www.palmorquay.com/
http://www.quillbrook.com/
the hotel is a simple hotel in a small town near a lot of ecological tourism attractions and in the heart of a small town beside the biggest lake in Guatemala. A website that brings out the colors of nature is what I'm looking for.
brightquillo brightquillo
Hi Marolyn , Its my pleasure to submit my creative ideas in your project. I am really very happy to design your project. If you need any changes any of my design feel free to knock me, thanks. Best regards, Brightquillo Team
gridmoxie gridmoxie
DO you have logo?

```html
<!DOCTYPE html>
<html lang="en">
<head>
<meta charset="utf-8">
<title>Hotel Brisaverde</title>
<link href="https://fonts.googleapis.com/css2?family=Cormorant+Garamond:wght@500&family=Open+Sans:wght@400;700&family=Roboto:wght@400;500&family=Roboto+Condensed:wght@400;700&display=swap" rel="stylesheet">
<style>
  :root{
    --navy:#0e1e3e;
    --nav-band:#4a5877;
    --slate:#222a3a;
    --panel:rgba(232,232,238,.88);
    --ink:#1a2a4a;
    --text:#3a3a3a;
    --white:#ffffff;
    --line:#7a86a3;
  }
  *{margin:0;padding:0;box-sizing:border-box}
  html,body{width:799px;height:1200px;overflow:hidden;background:var(--white)}
  .page{position:relative;width:799px;height:1200px;font-family:"Open Sans",sans-serif}
  .abs{position:absolute}

  /* header */
  .site-header{left:0;top:0;width:799px;height:112px;background:var(--navy)}
  .site-header .band{left:0;top:72px;width:799px;height:40px;background:#13244a}
  .brand-mark{width:44px;height:44px;border:2px solid var(--white);border-radius:50%}
  .brand-name{font-family:"Cormorant Garamond",serif;font-weight:500;color:var(--white);text-transform:uppercase;white-space:nowrap;letter-spacing:.3px}
  .top-nav a{position:absolute;top:22px;font-family:"Roboto",sans-serif;font-size:11.5px;color:var(--white);text-decoration:none;letter-spacing:.4px}
  .search{left:451px;top:21.5px;width:107px;height:17px;background:var(--white);font-family:"Roboto",sans-serif;font-size:9.5px;color:#444;padding:3px 0 0 9px}
  .search svg{position:absolute;right:8px;top:4px}
  .main-nav{left:199px;top:72px;width:539px;height:28px;background:var(--nav-band);border-radius:4px}
  .main-nav a{position:absolute;top:7px;font-family:"Roboto",sans-serif;font-size:11.8px;color:var(--white);text-decoration:none;letter-spacing:.4px}

  /* hero */
  .hero{left:0;top:112px;width:799px;height:358px;background:
    radial-gradient(ellipse 22% 30% at 40% 52%, rgba(214,140,70,.95) 0%, rgba(190,110,50,.6) 60%, transparent 100%),
    radial-gradient(ellipse 35% 25% at 55% 12%, rgba(235,228,218,.85) 0%, transparent 100%),
    radial-gradient(ellipse 30% 35% at 70% 85%, rgba(230,225,220,.7) 0%, transparent 100%),
    radial-gradient(ellipse 18% 25% at 12% 80%, rgba(200,200,205,.55) 0%, transparent 100%),
    linear-gradient(90deg,#2e2420 0%,#6a5446 25%,#9a8676 55%,#b8a89a 80%,#d8ccc2 100%)}
  .hero-arrow{width:50px;height:53px;background:rgba(14,30,62,.85)}
  .booking{left:510px;top:173px;width:199px;height:225px;background:var(--panel)}
  .booking h2{position:absolute;left:19px;top:24px;font-family:"Roboto",sans-serif;font-weight:400;font-size:15px;color:var(--ink)}
  .booking .lbl{position:absolute;font-family:"Roboto",sans-serif;font-size:10.5px;color:var(--ink)}
  .booking .date{position:absolute;left:78px;width:59px;height:15px;background:var(--white);font-family:"Roboto",sans-serif;font-size:8.5px;color:#333;padding:2px 0 0 6px}
  .booking .cal{position:absolute;left:148px}
  .booking .sel{position:absolute;top:137px;width:31px;height:14px;background:var(--white);font-size:8.5px;color:#333;padding:1px 0 0 7px;font-family:"Roboto",sans-serif}
  .booking .sel svg{position:absolute;right:6px;top:5px}
  .booking .help{position:absolute;left:154px;top:137px;width:11px;height:14px;background:var(--navy);color:var(--white);font-size:9px;text-align:center;line-height:14px;font-family:"Roboto",sans-serif}
  .booking .per{position:absolute;left:0;width:100%;top:155px;text-align:center;padding-left:22px;font-family:"Roboto",sans-serif;font-size:8.5px;color:#444}
  .booking .cta{position:absolute;left:19px;top:174px;width:161px;height:23px;background:var(--navy);color:var(--white);font-family:"Roboto",sans-serif;font-size:11px;padding:4px 0 0 5px;letter-spacing:.3px}
  .booking .cta svg{position:absolute;right:7px;top:6px}

  /* features */
  .feature{width:221px}
  .feature .photo{width:221px;height:127px;border:2px solid var(--navy)}
  .feature h3{position:absolute;left:0;top:139px;width:221px;font-size:10.5px;font-weight:700;color:var(--navy);text-align:center;letter-spacing:.4px;white-space:nowrap}
  .feature p{position:absolute;left:0;top:161px;width:221px;font-size:9.8px;line-height:11.7px;color:var(--text)}
  .feature p span{display:block;white-space:nowrap;text-align:justify;text-align-last:justify}
  .feature p span.end{text-align:center;text-align-last:center}
  .feature .btn{position:absolute;left:28px;top:242px;width:166px;height:30px;background:var(--navy);border-radius:4px;color:var(--white);font-size:10.5px;font-weight:700;text-align:center;line-height:30px;letter-spacing:.3px}

  /* footer */
  .site-footer{left:0;top:846px;width:799px;height:354px;background:var(--navy)}
  .site-footer h4{position:absolute;top:11px;font-family:"Roboto Condensed",sans-serif;font-weight:700;font-size:15px;color:var(--white);letter-spacing:-.2px}
  .dash{left:0;top:40px;width:799px;border-top:1px dashed var(--line)}
  .vrule{width:1px;height:148px;background:linear-gradient(to bottom,transparent,#5a6888,transparent)}
  .links a{position:absolute;font-family:"Roboto Condensed",sans-serif;font-size:10.8px;color:var(--white);text-decoration:none;letter-spacing:-.2px}
  .email{left:229px;top:74px;width:144px;height:26px;background:var(--white);font-family:"Roboto Condensed",sans-serif;font-size:10.5px;color:#444;padding:6px 0 0 9px}
  .subscribe{left:373px;top:74px;width:79px;height:26px;background:var(--slate);font-family:"Roboto Condensed",sans-serif;font-size:10.5px;color:var(--white);text-align:center;line-height:26px}
  .social{width:19px;height:19px;background:var(--white);border-radius:3px}
  .foot-text{font-family:"Roboto Condensed",sans-serif;font-size:10.5px;color:var(--white);letter-spacing:-.2px;white-space:nowrap}
  .phone{left:482px;top:69px;width:53px;height:105px;border-radius:8px;background:#0a0a0c;border:1px solid #8a92a5}
  .phone .screen{position:absolute;left:3px;top:15px;width:45px;height:74px;background:linear-gradient(160deg,#2a2e38,#050507 45%,#15171c)}
  .phone .home{position:absolute;left:21px;top:92px;width:8px;height:8px;border:1px solid #6a7285;border-radius:50%}
  .store{width:65px;height:21px;background:#2a2f3a;border:1px solid #6a7285;border-radius:3px}
  .learn{left:571px;top:160px;width:61px;height:18px;background:var(--white);font-family:"Roboto",sans-serif;font-size:9.5px;color:#222;text-align:center;line-height:18px}
</style>
</head>
<body>
<div class="page">

  <header class="abs site-header">
    <div class="abs band"></div>
    <div class="abs brand-mark" style="left:90px;top:20px"></div>
    <div class="abs brand-name" style="left:40px;top:77px;width:147px;text-align:center;font-size:14px">Hotel Brisaverde</div>

    <nav class="top-nav">
      <a style="left:240px">HOME</a>
      <a style="left:297px">LOCATION</a>
      <a style="left:380px">CONTACT</a>
    </nav>
    <div class="abs search">Search
      <svg width="9" height="9" viewBox="0 0 10 10"><circle cx="4" cy="4" r="3" fill="none" stroke="#222" stroke-width="1.6"/><line x1="6.3" y1="6.3" x2="9.2" y2="9.2" stroke="#222" stroke-width="1.8"/></svg>
    </div>

    <nav class="abs main-nav">
      <a style="left:9px">ACCOMMODATION</a>
      <a style="left:141px">GOLF</a>
      <a style="left:194px">SPA</a>
      <a style="left:238px">DINING</a>
      <a style="left:306px">OCASIONS</a>
      <a style="left:392px">SERVICESS</a>
      <a style="left:482px">OFFERS</a>
    </nav>
  </header>

  <section class="abs hero" role="img" aria-label="Breakfast table with a basket of croissants, pastries, jam jars, silverware and a glass of juice"></section>

  <div class="abs hero-arrow" style="left:23px;top:251px">
    <svg width="50" height="53" viewBox="0 0 50 53"><polyline points="31,13 18,26.5 31,40" fill="none" stroke="#c8ccd6" stroke-width="4"/></svg>
  </div>
  <div class="abs hero-arrow" style="left:723px;top:251px;background:rgba(60,70,95,.8)">
    <svg width="50" height="53" viewBox="0 0 50 53"><polyline points="19,13 32,26.5 19,40" fill="none" stroke="#c8ccd6" stroke-width="4"/></svg>
  </div>

  <aside class="abs booking">
    <h2>Check Availability</h2>
    <span class="lbl" style="left:19px;top:52px">Check In</span>
    <span class="date" style="top:52px">03/03/2015</span>
    <svg class="cal" style="top:48px" width="17" height="18" viewBox="0 0 17 18"><rect x="1" y="3" width="15" height="14" fill="none" stroke="#1a2a4a" stroke-width="1.4"/><rect x="1" y="3" width="15" height="3" fill="#1a2a4a"/><line x1="5" y1="0.5" x2="5" y2="4" stroke="#1a2a4a" stroke-width="1.5"/><line x1="12" y1="0.5" x2="12" y2="4" stroke="#1a2a4a" stroke-width="1.5"/><path d="M1 9.5H16M1 13H16M5 6V17M8.5 6V17M12 6V17" stroke="#1a2a4a" stroke-width=".8"/></svg>
    <span class="lbl" style="left:19px;top:75px">Check Out</span>
    <span class="date" style="top:75px">03/04/2015</span>
    <svg class="cal" style="top:71px" width="17" height="18" viewBox="0 0 17 18"><rect x="1" y="3" width="15" height="14" fill="none" stroke="#1a2a4a" stroke-width="1.4"/><rect x="1" y="3" width="15" height="3" fill="#1a2a4a"/><line x1="5" y1="0.5" x2="5" y2="4" stroke="#1a2a4a" stroke-width="1.5"/><line x1="12" y1="0.5" x2="12" y2="4" stroke="#1a2a4a" stroke-width="1.5"/><path d="M1 9.5H16M1 13H16M5 6V17M8.5 6V17M12 6V17" stroke="#1a2a4a" stroke-width=".8"/></svg>
    <span class="lbl" style="left:19px;top:107px">Room(S)</span>
    <span class="lbl" style="left:71px;top:107px">Adults</span>
    <span class="lbl" style="left:119px;top:107px">Children</span>
    <span class="sel" style="left:19px">1<svg width="6" height="4" viewBox="0 0 6 4"><polyline points="0.5,0.5 3,3 5.5,0.5" fill="none" stroke="#333"/></svg></span>
    <span class="sel" style="left:70px">1<svg width="6" height="4" viewBox="0 0 6 4"><polyline points="0.5,0.5 3,3 5.5,0.5" fill="none" stroke="#333"/></svg></span>
    <span class="sel" style="left:119px">1<svg width="6" height="4" viewBox="0 0 6 4"><polyline points="0.5,0.5 3,3 5.5,0.5" fill="none" stroke="#333"/></svg></span>
    <span class="help">?</span>
    <span class="per">-Per Room-</span>
    <div class="cta">FIND THE BEST RATE
      <svg width="7" height="11" viewBox="0 0 7 11"><polyline points="1,1 5.5,5.5 1,10" fill="none" stroke="#fff" stroke-width="1.6"/></svg>
    </div>
  </aside>

  <article class="abs feature" style="left:49px;top:512px;height:272px">
    <div class="photo" role="img" aria-label="Hotel lobby lounge with leather armchairs and a bar" style="background:
      radial-gradient(ellipse 30% 40% at 50% 45%, rgba(200,160,80,.8), transparent),
      linear-gradient(180deg,#4a3a28 0%,#6a5034 45%,#4a2a26 75%,#2a1e1a 100%)"></div>
    <h3>SAY HELLO TO&nbsp; HOTEL BRISAVERDE</h3>
    <p><span>Lorem Ipsum is simply dummy text of the</span><span>printing and typesetting industry. Lorem Ipsum</span><span>has been the industry's standard dummy text</span><span class="end">ever since&nbsp; specimen book.</span></p>
    <div class="btn">LARN MORE ABOUT US</div>
  </article>

  <article class="abs feature" style="left:288px;top:512px;height:272px">
    <div class="photo" role="img" aria-label="Classic suite bedroom with drapes, chandelier and armchairs" style="background:
      radial-gradient(ellipse 35% 40% at 55% 30%, rgba(240,215,170,.85), transparent),
      linear-gradient(180deg,#c8a070 0%,#d8b07a 40%,#b07a48 75%,#8a5a34 100%)"></div>
    <h3>TAKE HOME THE PLESURE</h3>
    <p><span>Lorem Ipsum is simply dummy text of the</span><span>printing and typesetting industry. Lorem Ipsum</span><span>has been the industry's standard dummy text</span><span class="end">ever since&nbsp; specimen book.</span></p>
    <div class="btn">VISIT OUR SUITES</div>
  </article>

  <article class="abs feature" style="left:528px;top:512px;height:272px">
    <div class="photo" role="img" aria-label="Afternoon tea table with pastries on plates and a red teddy bear" style="background:
      radial-gradient(ellipse 20% 30% at 80% 40%, rgba(180,50,40,.75), transparent),
      radial-gradient(ellipse 45% 25% at 50% 85%, rgba(235,230,225,.8), transparent),
      linear-gradient(180deg,#8a7054 0%,#a88a6a 50%,#6a4a36 100%)"></div>
    <h3>WE SERVE AUTHENTIC CUISINE</h3>
    <p><span>Lorem Ipsum is simply dummy text of the</span><span>printing and typesetting industry. Lorem Ipsum</span><span>has been the industry's standard dummy text</span><span class="end">ever since&nbsp; specimen book.</span></p>
    <div class="btn">VIEW OUR MENUS</div>
  </article>

  <footer class="abs site-footer">
    <h4 style="left:50px">Contact Details</h4>
    <h4 style="left:235px">Newsletters &amp; Offers</h4>
    <h4 style="left:489px">Enjoy Our Mobile App!</h4>
    <div class="abs dash"></div>

    <nav class="links">
      <a style="left:49px;top:55px">Corporate</a>
      <a style="left:49px;top:75px">Responsibility</a>
      <a style="left:49px;top:95px">Travel Agent</a>
      <a style="left:49px;top:115px">Affiliate Program</a>
      <a style="left:49px;top:135px">Press Room</a>
      <a style="left:149px;top:55px">Site Index</a>
      <a style="left:149px;top:75px">Help</a>
      <a style="left:149px;top:95px">Contact us</a>
      <a style="left:149px;top:115px">Careers</a>
    </nav>

    <div class="abs vrule" style="left:211px;top:54px"></div>
    <div class="abs vrule" style="left:469px;top:54px"></div>

    <div class="abs email">Your email address</div>
    <div class="abs subscribe">Subscribe</div>
    <div class="abs social" style="left:229px;top:119px"></div>
    <div class="abs social" style="left:259px;top:119px"></div>
    <div class="abs social" style="left:288px;top:119px"></div>
    <div class="abs social" style="left:318px;top:119px"></div>
    <div class="abs foot-text" style="left:231px;top:150px">Share your stories on Hotel Brisaverde.com</div>

    <div class="abs phone" role="img" aria-label="Smartphone showing the hotel app"><div class="screen"></div><div class="home"></div></div>
    <div class="abs" style="left:570px;top:69px;font-family:'Roboto',sans-serif;font-size:11px;line-height:13px;color:var(--white)">Unlimited access to the world of<br>Quillbrook wherever you go.</div>
    <div class="abs store" style="left:570px;top:107px"></div>
    <div class="abs store" style="left:570px;top:130px"></div>
    <div class="abs learn">Learn More</div>

    <div class="abs brand-mark" style="left:377px;top:242px"></div>
    <div class="abs brand-name" style="left:250px;top:294px;width:299px;text-align:center;font-size:17px">Hotel Brisaverde</div>
    <div class="abs foot-text" style="left:0;top:321px;width:799px;text-align:center">All Rights Reserved By&nbsp; @ Brightquillo.Com</div>
  </footer>

</div>
</body>
</html>
```